Exec Conference Design Concept

We need to refresh & update nonprofit association graphic design for annual meeting. The graphics will be used to promote the event primarily through digital communications & social media. Other materials we generate for this event are the agenda & billboard content. You can view the existing design at www.lorvamakers.example under Events.

The target audience is primarily male, ages 35-60 in executive positions in C-Corps. The conference topics center on manufacturing regulations, marketing trends, and the economy. This conference has been around almost 30 years so we need something to invigorate potential registrants that will get their attention. It still needs to be professional and business-like.

In addition to a new design concept we would like to update the color palette. We’ve attached some mood boards with potential color & font suggestions. Our company logo is also attached and is the only design element tied to our branding that cannot be changed.

Designs should be energetic and sophisticated. Ideally, we would like the designs in Adobe Indesign or Photoshop. However, we can work with Illustrator.

Target Market(s)

Male business executives age 35-60.

Industry/Entity Type

Polystyrene manufacturing industry supply chain.

Other font styles liked:
• I usually prefer sans serif

Requirements
Must have
• Focus points to draw attention to higher level informational units. For example, some people will only read the headers and not detailed copy.
Nice to have
• Ways to insert bonus content that don’t over power other content. I like to see a good use of white space to enhance readability.

```html
<!DOCTYPE html>
<html lang="en">
<head>
<meta charset="utf-8">
<title>Lorva Expo 2026 — Advancing Manufacturing Together</title>
<link rel="stylesheet" href="https://fonts.googleapis.com/css2?family=Italiana&family=Merriweather:wght@400&family=Barlow+Semi+Condensed:wght@500;700&family=Barlow:wght@700;800&display=swap">
<style>
  :root {
    --teal: #1f5a5d;
    --olive: #a2a237;
    --brown: #5d2e1e;
    --sand: #ddd6c8;
    --ink: #111111;
    --cream: #f1ebe0;
    --display: "Italiana", "Times New Roman", serif;
    --serif: "Merriweather", Georgia, serif;
    --sans: "Barlow Semi Condensed", "Arial Narrow", sans-serif;
    --heavy: "Barlow", Arial, sans-serif;
  }
  * { box-sizing: border-box; margin: 0; padding: 0; }
  html, body { width: 852px; height: 1200px; overflow: hidden; background: var(--sand); }
  .poster { position: relative; width: 852px; height: 1200px; background: var(--sand); overflow: hidden; }

  .top-band { position: absolute; left: 0; top: 0; width: 852px; height: 135px; background: var(--teal); }

  .event-mark {
    position: absolute; left: 290px; top: 0; width: 272px; height: 240px;
    background: var(--olive); border-bottom-right-radius: 34px;
    display: flex; flex-direction: column; align-items: center; justify-content: center;
    color: #ffffff; font-family: var(--heavy); font-weight: 800; text-align: center;
  }
  .event-mark .name { font-size: 62px; line-height: 0.95; letter-spacing: 1px; }
  .event-mark .year { font-size: 34px; line-height: 1.2; letter-spacing: 4px; }
  .event-mark .site { font-size: 17px; margin-top: 6px; letter-spacing: 0.2px; }

  .headline {
    position: absolute; left: 0; top: 245px; width: 852px; text-align: center;
    font-family: var(--display); font-size: 52px; color: var(--brown); letter-spacing: 0.5px;
  }
  .topics { position: absolute; left: 148px; top: 325px; list-style: none; }
  .topics li {
    font-family: var(--serif); font-size: 30px; line-height: 45px; color: var(--teal); position: relative; padding-left: 26px;
  }
  .topics li::before {
    content: ""; position: absolute; left: 0; top: 20px; width: 9px; height: 9px; border-radius: 50%; background: var(--brown);
  }

  .agenda { position: absolute; left: 0; top: 480px; width: 852px; height: 242px; background: var(--brown); }
  .agenda-title {
    position: absolute; left: 0; top: 26px; width: 852px; text-align: center;
    font-family: var(--display); font-size: 52px; color: var(--cream);
  }
  .agenda-item { position: absolute; top: 122px; width: 250px; }
  .agenda-item h3 {
    font-family: var(--sans); font-weight: 500; font-size: 15px; letter-spacing: 0.6px; color: var(--olive); margin-bottom: 12px;
  }
  .agenda-item p { font-family: var(--serif); font-size: 13.5px; line-height: 19px; color: var(--cream); }
  .agenda-item.regulatory { left: 58px; }
  .agenda-item.economic { left: 308px; }
  .agenda-item.communication { left: 574px; }

  .register {
    position: absolute; left: 265px; top: 762px; width: 341px; height: 80px; border-radius: 14px;
    background: var(--olive); color: var(--teal); font-family: var(--heavy); font-weight: 700;
    font-size: 36px; letter-spacing: 2px; display: flex; align-items: center; justify-content: center; text-decoration: none;
  }
  .speakers-title {
    position: absolute; left: 0; top: 850px; width: 852px; text-align: center;
    font-family: var(--display); font-size: 56px; color: var(--brown);
  }
  .swatch { position: absolute; top: 918px; width: 150px; text-align: center; }
  .swatch .dot { width: 98px; height: 98px; border-radius: 50%; margin: 0 auto; }
  .swatch .code { font-family: var(--heavy); font-weight: 700; font-size: 27px; letter-spacing: 2px; margin-top: 14px; }
  .swatch.black { left: 42px; } .swatch.black .dot { background: var(--ink); } .swatch.black .code { color: var(--ink); }
  .swatch.olive { left: 251px; } .swatch.olive .dot { background: var(--olive); } .swatch.olive .code { color: var(--olive); }
  .swatch.brown { left: 464px; } .swatch.brown .dot { background: var(--brown); } .swatch.brown .code { color: var(--brown); }
  .swatch.teal { left: 674px; } .swatch.teal .dot { background: var(--teal); } .swatch.teal .code { color: var(--teal); }

  .contact-bar {
    position: absolute; left: 0; top: 1082px; width: 852px; height: 76px; background: var(--teal);
    display: flex; align-items: center; padding-left: 16px;
  }
  .contact { display: flex; align-items: center; color: var(--cream); font-size: 25px; margin-right: 18px; }
  .contact svg { margin-right: 10px; flex: none; }
  .contact.phone { font-family: var(--sans); font-weight: 500; }
  .contact.email, .contact.web { font-family: var(--serif); font-size: 22px; }
</style>
</head>
<body>
<main class="poster">
  <div class="top-band"></div>

  <header class="event-mark">
    <span class="name">LORVA</span>
    <span class="year">2026</span>
    <span class="name">EXPO</span>
    <span class="site">www.lorvamakers.example</span>
  </header>

  <h1 class="headline">Advancing Manufacturing Together</h1>
  <ul class="topics">
    <li>Regulatory Updates</li>
    <li>Economic Trends</li>
    <li>Effective Communication Strategies</li>
  </ul>

  <section class="agenda">
    <h2 class="agenda-title">Conference Agenda Highlights</h2>
    <div class="agenda-item regulatory">
      <h3>REGULATORY UPDATES</h3>
      <p>Get the latest updates<br>on regulatory compliance<br>and industry requirements.</p>
    </div>
    <div class="agenda-item economic">
      <h3>ECONOMIC TRENDS</h3>
      <p>Hear from industry<br>economists on trends<br>shaping the manufacturing sector.</p>
    </div>
    <div class="agenda-item communication">
      <h3>COMMUNICATION STRATEGIES</h3>
      <p>Learn best practices for<br>effective communication in<br>today's regulatory environment.</p>
    </div>
  </section>

  <a class="register" href="#register">REGISTER NOW</a>

  <h2 class="speakers-title">Featured Speakers</h2>
  <div class="swatch black"><div class="dot"></div><div class="code">#00000</div></div>
  <div class="swatch olive"><div class="dot"></div><div class="code">#00000</div></div>
  <div class="swatch brown"><div class="dot"></div><div class="code">#00000</div></div>
  <div class="swatch teal"><div class="dot"></div><div class="code">#00000</div></div>

  <footer class="contact-bar">
    <div class="contact phone">
      <svg width="36" height="36" viewBox="0 0 24 24" aria-hidden="true"><path fill="#a2a237" d="M6.6 10.8a15.2 15.2 0 0 0 6.6 6.6l2.2-2.2a1 1 0 0 1 1-.25 11.4 11.4 0 0 0 3.6.57 1 1 0 0 1 1 1V20a1 1 0 0 1-1 1A17 17 0 0 1 3 4a1 1 0 0 1 1-1h3.5a1 1 0 0 1 1 1c0 1.25.2 2.45.57 3.57a1 1 0 0 1-.25 1z"/></svg>
      (123) 456-7890
    </div>
    <div class="contact email">
      <svg width="36" height="28" viewBox="0 0 36 28" aria-hidden="true"><rect x="2" y="2" width="32" height="24" fill="none" stroke="#a2a237" stroke-width="3"/><path d="M2 2 L18 16 L34 2 M2 26 L13 12 M34 26 L23 12" fill="none" stroke="#a2a237" stroke-width="3"/></svg>
      info@lorvaexpo.example
    </div>
    <div class="contact web">
      <svg width="30" height="30" viewBox="0 0 30 30" aria-hidden="true"><g fill="none" stroke="#a2a237" stroke-width="2.5"><circle cx="15" cy="15" r="13"/><ellipse cx="15" cy="15" rx="6" ry="13"/><path d="M2 15h26M4 8h22M4 22h22"/></g></svg>
      www.lorvaexpo.example
    </div>
  </footer>
</main>
</body>
</html>
```